Willowmere Counseling (Endure - Mend - Flourish) - Double Sided Business Card

I would like a 2-sided business card. Front: Matte Black or Navy with Logo & Tagline. Back: Name, Address, Phone Number, Email, & Website (maybe would like to include a small map pin-pointing location); Prefer front to be a gold/silver foil (iridescent); Back prefer white or light colored background with lettering that is easy to read and simple

Target Market(s)

Individuals & Couples (13 y.o. - ALL Adults); High end clientele

Industry/Entity Type

Licensed Professional Counselor (Mental Health)

Contact Information for Business Card

Name: Willowmere Counseling; Tagline: Endure - Mend - Flourish; Address: 3870 N. Garrick Ave., Suite 214, Fort Worth, TX 76132; Phone: (214) 555-0187; Website: www.WillowmereCounseling.example

Font styles to use
Serif

Requirements
Must have
• Logo on Front (Large) prefer gold/silver foil on a matte dark color (i.e. black, navy, etc.); Back of Card: All other relevant information

```html
<!DOCTYPE html>
<html lang="en">
<head>
<meta charset="utf-8">
<title>Willowmere Counseling – Business Card</title>
<link href="https://fonts.googleapis.com/css2?family=Cinzel:wght@500;600;700&display=swap" rel="stylesheet">
<style>
  :root {
    --page: #ffffff;
    --card-front: #222222;
    --card-back: #1e1c1d;
    --gold: #d4b85a;
    --ink-light: #f4f2ee;
  }
  * { margin: 0; padding: 0; box-sizing: border-box; }
  html, body { width: 1034px; height: 1200px; overflow: hidden; background: var(--page); }
  body { position: relative; font-family: "Cinzel", Georgia, serif; }

  .card {
    position: absolute; left: 71px; width: 904px; height: 515px; border-radius: 17px;
  }
  .card--front { top: 62px; background: var(--card-front); }
  .card--back { top: 620px; background: var(--card-back); }

  .brand-ring { position: absolute; }
  .card--front .brand-ring { left: 392px; top: 136px; }
  .card--back .brand-ring { left: 397px; top: 82px; }

  .front-name {
    position: absolute; left: 0; right: 0; top: 272px; text-align: center;
    color: var(--gold); font-weight: 600; line-height: 1;
  }
  .front-name .line-1 { display: block; font-size: 48px; letter-spacing: 0.5px; }
  .front-name .line-2 {
    display: flex; align-items: center; justify-content: center; gap: 8px;
    font-size: 24px; letter-spacing: 5px; margin-top: 6px;
  }
  .front-name .line-2::before,
  .front-name .line-2::after {
    content: ""; width: 88px; height: 4px; background: var(--gold);
  }
  .front-name .line-2::after { margin-left: -5px; }

  .front-tagline {
    position: absolute; left: 0; right: 0; top: 448px; text-align: center;
    color: var(--gold); font-size: 28px; font-weight: 600; letter-spacing: 0.5px;
  }

  .back-identity {
    position: absolute; right: 518px; top: 290px; text-align: right;
    color: var(--ink-light); font-weight: 600; line-height: 1;
  }
  .back-identity .name-1 { display: block; font-size: 38px; }
  .back-identity .name-2 { display: block; font-size: 34px; margin-top: 10px; }
  .back-identity .tagline { display: block; font-size: 19px; margin-top: 12px; letter-spacing: 0.8px; white-space: nowrap; }

  .contact-list { position: absolute; left: 0; top: 0; width: 904px; height: 515px; list-style: none; }
  .contact-item { position: absolute; left: 440px; width: 450px; height: 54px; }
  .contact-icon { position: absolute; left: 0; top: 0; width: 24px; height: 24px; }
  .contact-text {
    position: absolute; left: 72px; top: 0; color: var(--ink-light);
    font-size: 19px; font-weight: 600; line-height: 27px; white-space: nowrap;
  }
  .contact-item--address { top: 276px; }
  .contact-item--address .contact-icon { top: 8px; }
  .contact-item--phone { top: 356px; }
  .contact-item--web { top: 410px; }
  .contact-item--web .contact-text { font-size: 16px; letter-spacing: 0.2px; }
</style>
</head>
<body>

<section class="card card--front" aria-label="Card front">
  <svg class="brand-ring" width="120" height="120" viewBox="0 0 120 120" aria-hidden="true">
    <circle cx="60" cy="60" r="54" fill="none" stroke="var(--gold)" stroke-width="6"/>
  </svg>
  <h1 class="front-name"><span class="line-1">WILLOWMERE</span><span class="line-2">COUNSELING</span></h1>
  <p class="front-tagline">ENDURE - MEND - FLOURISH</p>
</section>

<section class="card card--back" aria-label="Card back">
  <svg class="brand-ring" width="120" height="120" viewBox="0 0 120 120" aria-hidden="true">
    <circle cx="60" cy="60" r="54" fill="none" stroke="var(--gold)" stroke-width="6"/>
  </svg>

  <div class="back-identity">
    <span class="name-1">Willowmere</span>
    <span class="name-2">Counseling</span>
    <span class="tagline">Endure - Mend - Flourish</span>
  </div>

  <ul class="contact-list">
    <li class="contact-item contact-item--address">
      <svg class="contact-icon" viewBox="0 0 24 24" fill="none" stroke="var(--gold)" stroke-width="1.4" aria-hidden="true">
        <path d="M12 22s-7-7.5-7-12.5a7 7 0 0 1 14 0C19 14.5 12 22 12 22z"/>
        <circle cx="12" cy="9.5" r="2.6"/>
      </svg>
      <span class="contact-text">3870 N. Garrick Ave., Suite 214,<br>Fort Worth, TX 76132</span>
    </li>
    <li class="contact-item contact-item--phone">
      <svg class="contact-icon" viewBox="0 0 24 24" fill="none" stroke="var(--gold)" stroke-width="1.4" aria-hidden="true">
        <path d="M5 3h4l2 5-2.5 1.5a11 11 0 0 0 6 6L16 13l5 2v4a2 2 0 0 1-2 2A17 17 0 0 1 3 5a2 2 0 0 1 2-2z"/>
      </svg>
      <span class="contact-text">(214) 555-0187</span>
    </li>
    <li class="contact-item contact-item--web">
      <svg class="contact-icon" viewBox="0 0 24 24" fill="none" stroke="var(--gold)" stroke-width="1.4" aria-hidden="true">
        <circle cx="12" cy="12" r="10"/>
        <ellipse cx="12" cy="12" rx="4.5" ry="10"/>
        <path d="M2 12h20M4 7h16M4 17h16"/>
      </svg>
      <span class="contact-text">www.WillowmereCounseling.example</span>
    </li>
  </ul>
</section>

</body>
</html>
```